female stress management consultant, doctor, Health & Well-being coach needs a wordpress theme

I am a Stress management consultant, General Practitioner and Health and Well-Being coach who is targeting mainly surgeries/hospitals and corporate business.
I have my own URL drhelgabrunsvik.com and the hosting.
I need a WordPress Website that is easy to maintain and edit to regularly change the content (copy/pictures/action buttons/banners).
I want my website to look professional and elegant for corporate businesses and managers to feel they can trust me and my expertise. At the same time, the website should have a warm and welcoming feel to it. It should feel uplifting and very positive.
I am open to colour suggestions, but please incorporate the following two colours: #F18877 and #D2BB7A. For fonts I prefer grey over black (like #777777).
The website needs to create an impression of "know like and trust".
The website should have a sign-up button for a newsletter, multiple contact buttons over the home page - to write an email to me, contact details top and bottom and the possibility to have a video on the home page top instead of a picture (Best would be that I can change from picture to video to picture in the future without needing a designer). A video that can run in the background with text laid over. A bit like on this website from Tessa Vanrijn: https://www.tessavanrijn.com.
I need 5 pages: Home, About, Services, Contact, free resources. I do NOT need an e-commerce or booking facility as I will neither sell nor let people book through my website. I don't need a blog either.
All the pages need to have a link to my other website (brightpathdaily.co.uk) and it needs to state that the linked website (brightpathdaily) is my website with a blog and for private customers.
Please use the photos I attached if possible. Me with the dogs for the "about" section.

Websites I like: https://www.olgabkr.com, tessavanrijn.com, https://ruthpembly.com (this site is too dark for my liking, but the layout has a simple navigation layout, the important buttons are right up at the side (WorkLattice/social media/CTA), is minimalistic - hence easy to find the important bits).

Target Market(s)

surgeries/doctor offices, hospitals, corporate business

Industry/Entity Type

Health and well-being

Coding

Coded - Design and coding required

Number of Pages Required

5+ page

Font styles to use
Sans Serif

Requirements
Must have
• see project description
Nice to have
• see project description

```html
<!DOCTYPE html>
<html lang="en">
<head>
<meta charset="utf-8">
<title>Dr. Helga Brunsvik – Stress Management, GP &amp; Well-Being Coach</title>
<link rel="stylesheet" href="https://fonts.googleapis.com/css2?family=Crimson+Text:ital,wght@0,400;0,600;1,400;1,600&family=Libre+Baskerville:wght@700&family=Roboto:wght@400;500;700&display=swap">
<style>
:root{
  --coral:#F18877;
  --gold:#D2BB7A;
  --pink:#F3C6C2;
  --grey:#777777;
  --ink:#222222;
  --light:#f4f4f4;
  --footer:#353535;
  --footer-dark:#242424;
  --serif:"Crimson Text",Georgia,serif;
  --sans:"Roboto",Arial,sans-serif;
}
*{margin:0;padding:0;box-sizing:border-box}
html,body{width:1200px;height:3444px;overflow:hidden}
body{position:relative;font-family:var(--sans);color:var(--grey);background:#fff}
.abs{position:absolute}
.btn{position:absolute;display:flex;align-items:center;justify-content:center;font-family:var(--sans);font-weight:700;text-transform:uppercase;letter-spacing:.3px}
.btn-coral{background:var(--coral);color:#fff;font-size:10.5px}
.btn-outline{background:#fff;border:2px solid var(--coral);color:var(--ink);font-size:11.5px;text-transform:none;font-weight:500}
.btn-outline-grey{background:#fff;border:2px solid #aaa;color:var(--ink);font-size:11.5px;font-weight:500}

/* header */
.logo{left:214px;top:12px;display:flex;align-items:center;gap:8px}
.logo-dot{width:26px;height:26px;border-radius:50%;background:var(--gold)}
.logo-name{font-family:var(--sans);font-weight:500;font-size:19px;color:var(--coral);line-height:1}
.logo-tag{font-size:10px;color:var(--gold);font-style:italic;margin-top:2px}
.nav{top:22px;font-size:10.5px;font-weight:700;color:var(--ink);letter-spacing:.3px}

/* hero */
.hero{left:0;top:0;width:1200px;height:575px;background:linear-gradient(100deg,#fff 0%,#fdf9f2 35%,#f2e6cf 62%,#e7d2ae 80%,#d9b98a 100%)}
.hero-ground{left:0;top:500px;width:1200px;height:75px;background:linear-gradient(180deg,rgba(150,120,80,0) 0%,#8a6c4a 60%,#6f5438 100%)}
.hero-title{left:215px;top:130px;font-family:"Libre Baskerville",Georgia,serif;font-weight:700;font-size:42px;line-height:51px;color:var(--ink)}
.hero-text{left:216px;top:295px;width:420px;font-size:15px;line-height:22.5px;color:#444}

/* newsletter */
.news{left:0;top:575px;width:1200px;height:106px;background:var(--pink)}
.news-title{left:258px;top:594px;font-family:var(--serif);font-style:italic;font-size:27px;color:#333}
.news-sub{left:258px;top:629px;width:300px;font-size:10px;line-height:15px;color:#7a6b6b}
.news-input{left:632px;top:609px;width:238px;height:37px;background:#fff;border:1px solid #e4b1ab;font-size:11px;font-style:italic;color:#999;padding:12px}

/* about */
.about-photo{left:0;top:681px;width:605px;height:431px;background:linear-gradient(180deg,#c8d9e6 0%,#8fa9bf 35%,#4e6a86 60%,#6b7d8a 85%,#b9b9b5 100%)}
.hello{left:660px;top:745px;font-size:8.5px;font-weight:700;color:var(--ink);letter-spacing:1px}
.about-title{left:660px;top:768px;font-family:var(--serif);font-style:italic;font-size:40px;line-height:42px;color:var(--ink)}
.about-title em{color:var(--coral);font-style:italic}
.about-text{left:660px;top:867px;width:330px;font-size:13px;line-height:20px;color:var(--grey)}

/* services */
.services{left:0;top:1112px;width:1200px;height:267px;background:var(--gold)}
.divider{top:1112px;width:1px;height:267px;background:rgba(255,255,255,.35)}
.svc{top:1145px;width:232px;text-align:center}
.svc-icon{width:54px;height:54px;border-radius:50%;background:#fff;margin:0 auto;display:flex;align-items:center;justify-content:center}
.svc-title{font-family:var(--serif);font-style:italic;font-weight:600;font-size:19px;color:var(--ink);margin-top:8px}
.svc-text{font-size:11px;line-height:18.7px;color:#4a4231;margin-top:4px}
.svc-more{font-size:11px;color:#fff;margin-top:9px}

/* help band */
.help{left:0;top:1379px;width:1200px;height:196px;background:var(--light)}
.help-photo{left:640px;top:1379px;width:560px;height:196px;background:linear-gradient(90deg,rgba(244,244,244,0) 0%,#f6e4c4 25%,#f0c27e 55%,#d9a05a 80%,#f2e4cc 100%)}
.eyebrow{font-size:8.5px;font-weight:700;letter-spacing:1px;text-transform:uppercase}
.help-title{left:213px;top:1437px;font-family:var(--serif);font-style:italic;font-weight:600;font-size:35px;color:var(--ink)}

/* summit */
.summit-1{left:0;top:1615px;width:1200px;text-align:center;font-family:var(--serif);font-style:italic;font-size:33px;color:var(--ink)}
.summit-2{left:0;top:1652px;width:1200px;text-align:center;font-family:var(--serif);font-style:italic;font-size:33px;color:var(--coral)}
.video{left:333px;top:1711px;width:534px;height:298px;background:linear-gradient(135deg,#ece7e1 0%,#d9d2ca 45%,#b9b3c3 70%,#4b4656 100%)}
.play{left:573px;top:1833px;width:54px;height:54px;border-radius:50%;background:#fff;display:flex;align-items:center;justify-content:center}

/* resources */
.resources{left:0;top:2060px;width:1200px;height:533px;background:var(--pink)}
.res-title{left:0;top:2128px;width:1200px;text-align:center;font-family:var(--serif);font-style:italic;font-size:36px;color:var(--ink)}
.card{top:2194px;width:250px;height:348px;background:#fff}
.card-img{width:250px;height:153px}
.card-title{position:absolute;left:19px;top:168px;font-family:var(--serif);font-style:italic;font-weight:600;font-size:17px;color:var(--ink)}
.card-text{position:absolute;left:19px;top:197px;width:215px;font-size:9.5px;line-height:16.3px;color:var(--grey)}

/* testimonials */
.test-title{left:0;top:2640px;width:1200px;text-align:center;font-family:var(--serif);font-style:italic;font-size:39px;color:var(--ink)}
.test-lead{left:0;top:2708px;width:1200px;text-align:center;font-family:var(--serif);font-style:italic;font-size:17px;color:var(--ink)}
.test-body{left:272px;top:2739px;width:656px;text-align:center;font-style:italic;font-size:13px;line-height:20px;color:var(--grey)}
.avatar{left:535px;top:2839px;width:51px;height:57px;background:linear-gradient(180deg,#cbd6df,#8fa6b8)}
.dot{top:2926px;width:9px;height:9px;background:var(--grey)}

/* cta */
.cta{left:0;top:2986px;width:1200px;height:226px;background:var(--coral)}
.cta-text{left:0;top:3028px;width:1200px;text-align:center;font-family:var(--serif);font-style:italic;font-size:35px;line-height:38px;color:#fff}

/* footer */
.footer{left:0;top:3212px;width:1200px;height:209px;background:var(--footer)}
.footer-bar{left:0;top:3421px;width:1200px;height:23px;background:var(--footer-dark);color:#aaa;font-size:8.5px;text-align:center;line-height:23px}
.foot-quote{left:214px;top:3305px;width:230px;font-style:italic;font-size:12.5px;line-height:17.5px;color:#bbb}
.foot-links{top:3249px;font-size:10.5px;line-height:22.7px;color:#bbb}
.foot-news{left:740px;top:3250px;font-family:var(--serif);font-style:italic;font-size:21px;line-height:23px;color:#ccc}
.foot-input{left:738px;top:3304px;width:168px;height:31px;background:#757575;color:#eee;font-size:10px;padding:10px 12px}
.social{top:3351px;width:24px;height:24px;border-radius:50%;border:1.5px solid #bbb}
.social-label{top:3380px;width:50px;text-align:center;font-size:6.5px;color:#aaa}
</style>
</head>
<body>

<!-- Hero -->
<div class="abs hero" role="img" aria-label="Photo of a woman meditating cross-legged at sunrise by the water"></div>
<div class="abs hero-ground" role="img" aria-label="Sandy ground in warm morning light"></div>

<header>
  <div class="abs logo">
    <span class="logo-dot"></span>
    <div>
      <div class="logo-name">Dr. Helgabrunsvik</div>
      <div class="logo-tag">Create a life you love living</div>
    </div>
  </div>
  <nav>
    <span class="abs nav" style="left:463px">HOME</span>
    <span class="abs nav" style="left:519px">ABOUT</span>
    <span class="abs nav" style="left:582px">SERVICES</span>
    <span class="abs nav" style="left:660px">FREE RESOURCES</span>
    <span class="abs nav" style="left:779px">CONTACT</span>
    <a class="btn btn-coral" style="left:844px;top:15px;width:143px;height:28px">Get a free consultant</a>
  </nav>
</header>

<section>
  <h1 class="abs hero-title">Live a Healthy<br>&amp; Best Life With<br>Full of Joy!</h1>
  <p class="abs hero-text">I am a Stress management consultant, General Practitioner and Health and Well-Being coach who is targeting mainly surgeries/hospitals and corporate business.</p>
  <a class="btn btn-coral" style="left:217px;top:381px;width:143px;height:30px">Get a free consultant</a>
</section>

<!-- Newsletter -->
<section>
  <div class="abs news"></div>
  <h2 class="abs news-title">Subscribe to Our Newsletter</h2>
  <p class="abs news-sub">Get regular inspiration for the Health and Well-Being, and keep up with the healthcare stories that matter.</p>
  <div class="abs news-input">Your Email Address</div>
  <a class="btn btn-coral" style="left:870px;top:609px;width:79px;height:37px">Subscribe</a>
</section>

<!-- About -->
<section>
  <div class="abs about-photo" role="img" aria-label="Photo of a woman meditating on a pier beside a lake fountain"></div>
  <div class="abs hello">HELLO !</div>
  <h2 class="abs about-title">I’m <em>Doctor<br>Helgabrunsvik.</em></h2>
  <p class="abs about-text">With over 30 years of being a doctor, I’ve met countless people facing ongoing health issues and struggles that couldn’t be solved solely through conventional medicine. That’s why it’s so important to embrace a holistic approach in our quest for balance, shifting from discomfort to vitality and contentment.</p>
  <a class="btn btn-outline" style="left:660px;top:1014px;width:113px;height:32px">Read More</a>
</section>

<!-- Services -->
<section>
  <div class="abs services"></div>
  <div class="abs divider" style="left:468px"></div>
  <div class="abs divider" style="left:730px"></div>

  <div class="abs svc" style="left:217px">
    <div class="svc-icon">
      <svg width="30" height="30" viewBox="0 0 30 30" fill="none" stroke="#F18877" stroke-width="2.4" stroke-linecap="round">
        <path d="M7 4v8a6 6 0 0 0 12 0V4"/><path d="M13 18v3a5 5 0 0 0 10 0v-3"/><circle cx="23" cy="15" r="3"/>
      </svg>
    </div>
    <h3 class="svc-title">Consultant</h3>
    <p class="svc-text">I am Stress Management Consultant. If you’re feeling stuck, uncertain, or struggling with your health or well-being, one-on-one coaching can provide the guidance and support you need. Through working ...</p>
    <p class="svc-more">[ Read more... ]</p>
  </div>

  <div class="abs svc" style="left:483px">
    <div class="svc-icon">
      <svg width="30" height="30" viewBox="0 0 30 30" fill="none" stroke="#F18877" stroke-width="2.4" stroke-linejoin="round">
        <rect x="4" y="9" width="22" height="16" rx="3"/><path d="M11 9V6h8v3"/><path d="M15 13v8M11 17h8" stroke-linecap="round"/>
      </svg>
    </div>
    <h3 class="svc-title">General Practitioner</h3>
    <p class="svc-text">The Medical Doctor and General Practitioner, certified Health and Well-being Coach hold a doctorate degree in virology (PhD); I’m a Meditation teacher, Intentional Creativity Coach and Teacher, artist, friend, mum...</p>
    <p class="svc-more">[ Read more... ]</p>
  </div>

  <div class="abs svc" style="left:752px">
    <div class="svc-icon">
      <svg width="30" height="30" viewBox="0 0 30 30" fill="none" stroke="#F18877" stroke-width="2" stroke-linecap="round">
        <circle cx="15" cy="6" r="3"/><path d="M15 10v9M8 15l7-3 7 3M6 24c3-3 15-3 18 0"/>
      </svg>
    </div>
    <h3 class="svc-title">Health &amp; Well-Being Coach</h3>
    <p class="svc-text">I’m a Meditation teacher, Intentional Creativity Coach and Teacher, artist, friend, mum, and a humble human being who has a wealth of knowledge on how to lead a happy and healthy life. I offer a variety of engaging and...</p>
    <p class="svc-more">[ Read more... ]</p>
  </div>
</section>

<!-- I help you -->
<section>
  <div class="abs help"></div>
  <div class="abs help-photo" role="img" aria-label="Photo of a smiling woman in a sun hat with arms spread in golden sunlight"></div>
  <div class="abs eyebrow" style="left:213px;top:1423px;color:var(--coral)">Create a life you love living</div>
  <h2 class="abs help-title">I Help You Live Your Best Life</h2>
  <a class="btn btn-coral" style="left:214px;top:1501px;width:143px;height:28px">Get a free consultant</a>
</section>

<!-- Summit -->
<section>
  <h2 class="abs summit-1">It's never too late</h2>
  <h2 class="abs summit-2">Virtual Summit 2000</h2>
  <div class="abs video" role="img" aria-label="Video still of a group yoga class stretching on mats"></div>
  <div class="abs play">
    <svg width="22" height="24" viewBox="0 0 22 24"><path d="M3 2l17 10L3 22z" fill="#e8221b"/></svg>
  </div>
</section>

<!-- Free resources -->
<section>
  <div class="abs resources"></div>
  <div class="abs eyebrow" style="left:0;top:2107px;width:1200px;text-align:center;color:var(--ink)">Our free resources</div>
  <h2 class="abs res-title">that help you live your best life</h2>

  <article class="abs card" style="left:213px">
    <div class="card-img" role="img" aria-label="Photo of a healthy salad with a glass of white wine" style="background:linear-gradient(160deg,#8a98c8 0%,#c6cde4 50%,#f2f0ee 100%)"></div>
    <h3 class="card-title">Eat Well</h3>
    <p class="card-text">I’ve met countless people facing ongoing health issues and struggles that couldn’t be solved solely through conventional medicine. That’s why it’s so important to embrace a holistic approach in our quest for balance..</p>
    <a class="btn btn-outline-grey" style="left:19px;top:290px;width:114px;height:32px">Get Inspired</a>
  </article>

  <article class="abs card" style="left:475px">
    <div class="card-img" role="img" aria-label="Photo of a joyful woman with arms raised in a garden" style="background:linear-gradient(160deg,#4f7a3a 0%,#7fa25e 45%,#8f95c4 100%)"></div>
    <h3 class="card-title">Live Healthy</h3>
    <p class="card-text">The secret to living a joyful, vibrant life lies in nurturing every aspect of yourself, not just your physical body. Surprisingly, it’s easier as you might think to harmonize your body, mind, and spirit and experience optimal well-being...</p>
    <a class="btn btn-outline-grey" style="left:19px;top:290px;width:114px;height:32px">Get Inspired</a>
  </article>

  <article class="abs card" style="left:738px">
    <div class="card-img" role="img" aria-label="Close-up portrait photo of a smiling woman" style="background:linear-gradient(160deg,#5d6b4a 0%,#c9a78a 50%,#e4c8b2 100%)"></div>
    <h3 class="card-title">It’s Been So Easy</h3>
    <p class="card-text">They provide knowledge, support, and motivation for positive change. Engaging in these discussions connects you to a community, empowers you with insights, and promotes self-awareness. Get ready for</p>
    <a class="btn btn-outline-grey" style="left:19px;top:290px;width:114px;height:32px">Get Inspired</a>
  </article>
</section>

<!-- Testimonials -->
<section>
  <h2 class="abs test-title">Testimonials</h2>
  <h3 class="abs test-lead">Working with Dr Helga helped me to appreciate myself more.</h3>
  <p class="abs test-body">The workshop has allowed me to appreciate myself more. For what I am. The quality of delivery is what made the experience. Dr Helga’s understanding of the guided meditations helped enormously. Being in an exclusive, supportive and safe environment allowed me to get in touch with elements of myself that I was shy of. I’d love more people to be able to access this and to experience this quality of experience.</p>
  <div class="abs avatar" role="img" aria-label="Client portrait photo"></div>
  <div class="abs" style="left:599px;top:2850px;font-size:14px;color:var(--coral)">Mira T.</div>
  <div class="abs" style="left:599px;top:2868px;font-size:10.5px;color:var(--grey)">Private Client</div>
  <div class="abs dot" style="left:572px;background:var(--coral)"></div>
  <div class="abs dot" style="left:588px"></div>
  <div class="abs dot" style="left:604px"></div>
  <div class="abs dot" style="left:620px"></div>
</section>

<!-- CTA -->
<section>
  <div class="abs cta"></div>
  <h2 class="abs cta-text">Discover Simple Steps to Restore Your Happiness<br>and Health Today!</h2>
  <a class="btn" style="left:494px;top:3131px;width:212px;height:32px;background:#fff;color:var(--ink);font-size:10.5px">Get a free consultant today!</a>
</section>

<!-- Footer -->
<footer>
  <div class="abs footer"></div>
  <div class="abs logo" style="top:3251px">
    <span class="logo-dot"></span>
    <div>
      <div class="logo-name" style="font-size:22px">Helgabrunsvik</div>
      <div class="logo-tag" style="color:#bbb">Create a life you love living</div>
    </div>
  </div>
  <p class="abs foot-quote">The time that you invest in yourself, your health and your happiness will be the best investment you can make. You can’t buy happiness, but you can create it.</p>

  <div class="abs foot-links" style="left:469px">Home<br>About<br>Services<br>Coaching<br>Free Resources<br>Free Talk Health</div>
  <div class="abs foot-links" style="left:598px">Privacy Policy<br>Disclaimer<br>Health &nbsp;Advice<br>Virtual Summit<br>News &amp; Blog<br>Contact</div>

  <h3 class="abs foot-news">Join our newsletter to get<br>the latest news and tips.</h3>
  <div class="abs foot-input">Your Email Address</div>
  <a class="btn" style="left:906px;top:3304px;width:81px;height:31px;background:var(--gold);color:#fff;font-size:10px;text-transform:none;font-weight:500">Join Now</a>

  <span class="abs social" style="left:740px"></span>
  <span class="abs social" style="left:776px"></span>
  <span class="abs social" style="left:811px"></span>
  <span class="abs social" style="left:848px"></span>
  <span class="abs social" style="left:887px"></span>
  <span class="abs social-label" style="left:727px">FaceSpace</span>
  <span class="abs social-label" style="left:763px">Chirper</span>
  <span class="abs social-label" style="left:798px">WorkLattice</span>
  <span class="abs social-label" style="left:835px">Snapgram</span>
  <span class="abs social-label" style="left:874px">ViewTube</span>

  <div class="abs footer-bar">© 2023 Dr. Helga Brunsvik. All rights reserved. &nbsp;|&nbsp; Consultant, Coach and General Practitioner</div>
</footer>

</body>
</html>
```